Vital Spark Electrical in need of a business card design

We need a new business card designed for our electrical business. We have a logo already which I will attach below.
Would like the business card to be..
-BLACK background preferably, possibly white back ground behind logo if colours clash.
-White & Blue (logo blue) text
Something that makes the logo pop, & a modern look. Possibly minimal clean format.

REQUIRE:
-Logo on front & back

TEXT TO INCLUDE (ON ONE SIDE):

Tom Harlow
Director/Electrician
M: 0417 365 208
E:info@vitalsparkelectrical-example.com.au
W:www.vitalsparkelectrical-example.com.au
R.E.C 57318

Custom/New Homes
Renovations
Commercial Office/Shop Fit-outs
Communications & Security Cameras
Electric Vehicle Chargers
Airconditioning
Updates

Requirements
Nice to have
• Possibly even lighten the grey shades for the words 'Vital' & 'Spark' to be more easily read on a black background.

```html
<!DOCTYPE html>
<html lang="en">
<head>
<meta charset="utf-8">
<title>Vital Spark Electrical – Business Card</title>
<link rel="stylesheet" href="https://fonts.googleapis.com/css2?family=Encode+Sans+Condensed:wght@300;400;600&display=swap">
<style>
  :root {
    --page: #ffffff;
    --card-black: #000000;
    --pattern-tone: #1c1e21;
    --ink: #111111;
    --ink-soft: #2a2a2a;
    --brand-blue: #0aa8e0;
    --brand-grey: #5b6169;
    --rule: #1a1a1a;
  }
  * { margin: 0; padding: 0; box-sizing: border-box; }
  html, body { width: 846px; height: 1200px; overflow: hidden; background: var(--page); }
  body { position: relative; font-family: "Encode Sans Condensed", sans-serif; color: var(--ink); }

  .card { position: absolute; width: 504px; height: 280px; }

  /* Front */
  .card-front { left: 70px; top: 288px; background: var(--card-black); overflow: hidden; }
  .front-pattern {
    position: absolute; inset: 0;
    background: radial-gradient(ellipse at center, #26282c 0%, var(--pattern-tone) 45%, var(--card-black) 100%);
  }
  .front-brand {
    position: absolute; left: 0; right: 0; top: 0; bottom: 0;
    display: flex; align-items: center; justify-content: center; gap: 12px;
  }
  .brand-mark { width: 26px; height: 26px; background: var(--brand-blue); }
  .brand-name {
    font-weight: 600; font-size: 30px; letter-spacing: 0.2px; color: var(--brand-blue); white-space: nowrap;
  }

  /* Back */
  .card-back { left: 255px; top: 607px; height: 279px; background: #fff; border: 1.2px solid var(--rule); }
  .holder { position: absolute; left: 29px; top: 42px; }
  .holder-name { font-weight: 600; font-size: 22px; line-height: 1; letter-spacing: -0.3px; color: var(--ink); }
  .holder-role { font-weight: 400; font-size: 17px; line-height: 1; margin-top: 7px; color: var(--ink-soft); }

  .back-brand { position: absolute; right: 18px; top: 48px; display: flex; align-items: center; gap: 8px; }
  .back-brand .brand-mark { width: 18px; height: 18px; }
  .back-brand .brand-name { font-size: 21px; color: var(--brand-grey); }

  .contacts { position: absolute; left: 20px; top: 132px; list-style: none; }
  .contacts li { display: flex; align-items: center; height: 32.5px; font-weight: 300; font-size: 16px; color: var(--ink); white-space: nowrap; }
  .contacts li.long { font-size: 12.6px; letter-spacing: -0.1px; }
  .contacts svg { width: 16px; height: 16px; margin-right: 9px; flex: none; fill: var(--ink); }

  .divider { position: absolute; left: 262px; top: 131px; width: 2.5px; height: 122px; background: var(--rule); }

  .services { position: absolute; left: 276px; top: 131px; list-style: none; }
  .services li { font-weight: 300; font-size: 14.6px; line-height: 20px; color: var(--ink-soft); white-space: nowrap; }
</style>
</head>
<body>

<section class="card card-front" aria-label="Card front">
  <div class="front-pattern" role="img" aria-label="Dark repeating pattern of window outlines"></div>
  <div class="front-brand">
    <span class="brand-mark"></span>
    <span class="brand-name">Vital Spark Electrical</span>
  </div>
</section>

<section class="card card-back" aria-label="Card back">
  <div class="holder">
    <h1 class="holder-name">Tom Harlow</h1>
    <p class="holder-role">Director/Electrician</p>
  </div>

  <div class="back-brand">
    <span class="brand-mark"></span>
    <span class="brand-name">Vital Spark Electrical</span>
  </div>

  <ul class="contacts">
    <li>
      <svg viewBox="0 0 24 24" aria-hidden="true"><path d="M6.6 10.8a15.1 15.1 0 0 0 6.6 6.6l2.2-2.2c.3-.3.7-.4 1-.2 1.1.4 2.3.6 3.6.6.6 0 1 .4 1 1V20c0 .6-.4 1-1 1A17 17 0 0 1 3 4c0-.6.4-1 1-1h3.5c.6 0 1 .4 1 1 0 1.3.2 2.5.6 3.6.1.3 0 .7-.2 1z"/></svg>
      0417 365 208
    </li>
    <li class="long">
      <svg viewBox="0 0 24 24" aria-hidden="true"><path d="M3 6h18v12H3z M3 6l9 7 9-7" fill="none" stroke="#111" stroke-width="0"/><path d="M3 6h18l-9 7z"/><path d="M3 8l9 7 9-7v10H3z"/></svg>
      info@vitalsparkelectrical-example.com.au
    </li>
    <li class="long">
      <svg viewBox="0 0 24 24" aria-hidden="true"><circle cx="12" cy="12" r="9" fill="none" stroke="#111" stroke-width="1.8"/><ellipse cx="12" cy="12" rx="4" ry="9" fill="none" stroke="#111" stroke-width="1.6"/><path d="M3 12h18M5 7h14M5 17h14" stroke="#111" stroke-width="1.4"/></svg>
      www.vitalsparkelectrical-example.com.au
    </li>
    <li>
      <svg viewBox="0 0 24 24" aria-hidden="true"><path d="M12 3 2 12h3v9h5v-6h4v6h5v-9h3z"/></svg>
      R.E.C 57318
    </li>
  </ul>

  <div class="divider"></div>

  <ul class="services">
    <li>Custom/New Homes</li>
    <li>Renovations</li>
    <li>Commercial Office/Shop Fit-outs</li>
    <li>Communications &amp; Security Cameras</li>
    <li>Electric Vehicle Chargers</li>
    <li>Airconditioning</li>
  </ul>
</section>

</body>
</html>
```